KRILO is a 8-minute, fast-acting, chewable form of Moruvel

Description of Product Packaging
The name KRILO was specifically chosen because it describes the sound of sex and has the word 'hump' in the name. The KRILO logo is the actual letters, cracking the ground with such force that it shatters the foundation. The sides of the letters are pulsating to mimick the pulsating male genitalia. The marketing for KRILO should be geared towards male consumers -- specfically, younger men who will use this product for recreational purposes.

1) The word Krilo needs to be on each side of the box
2) Remove all pictures and focus on the product not the people
3) Main Focus should eye catching.

I would like you to design the packaging for the following receptacles:
1) Sample pack (contains 1 pill)
2) Standard box (contains one 10-pill blister pack)
3) Bottle / Box (contains 20 pills)
4) Bottle / Box (contains 50 pills)
5) Bottle / Box (contains 100 pills)
ANY HELPFUL CONTENT YOU WANT

Target Market(s)

Men 18 to 100

Industry/Entity Type

Product

Requirements
Must have
• Please incorporate the logo on each side/panel of the packaging.
• Please make sure the design includes spaces for the barcode and the dosage information.
• Slick, cool young focus design.
• No to sexual to cause embarrassment to buy.
Nice to have
• Since KRILO is a double-entendre, the tagline and copywriting should have a sense of playfulness and a sense of humor.
Should not have
• I do not want erotic images of couples on the packaging. Other images are acceptable as long as they are not lewd in nature.

```html
<!DOCTYPE html>
<html lang="en">
<head>
<meta charset="utf-8">
<title>KRILO Packaging</title>
<link rel="stylesheet" href="https://fonts.googleapis.com/css2?family=Quicksand:wght@400;700&display=swap">
<style>
  :root {
    --red: #d31a20;
    --red-dark: #9c0f14;
    --white: #ffffff;
    --ink: #141414;
    --silver-light: #f1f1f1;
    --silver-mid: #b9b9b9;
    --silver-dark: #8a8a8a;
    --bg-top: #d9d9d9;
    --bg-bottom: #ffffff;
  }
  html, body {
    margin: 0;
    padding: 0;
    width: 1200px;
    height: 1200px;
    overflow: hidden;
  }
  body {
    background: linear-gradient(180deg, var(--bg-top) 0%, var(--bg-bottom) 40%);
    font-family: "Quicksand", sans-serif;
    position: relative;
  }
  .panel {
    position: absolute;
    box-shadow: 0 10px 30px rgba(0,0,0,0.12);
    background: var(--white);
  }
  .panel svg { display: block; width: 100%; height: 100%; }
  .box-front     { left: 90px;  top: 150px; width: 300px; height: 460px; }
  .bottle-large  { left: 450px; top: 150px; width: 300px; height: 460px; }
  .bottle-small  { left: 810px; top: 150px; width: 300px; height: 460px; }
  .sample-inside { left: 420px; top: 700px; width: 170px; height: 280px; }
  .sample-front  { left: 610px; top: 700px; width: 170px; height: 280px; }
  .brand-name { font-family: "Quicksand", sans-serif; font-weight: 700; fill: var(--ink); }
  .big-num   { font-family: "Quicksand", sans-serif; font-weight: 400; fill: var(--white); }
  .minute    { font-family: "Quicksand", sans-serif; font-weight: 400; fill: var(--white); }
  .claim     { font-family: "Quicksand", sans-serif; font-weight: 400; fill: #3a3a3a; }
  .count     { font-family: "Quicksand", sans-serif; font-weight: 700; fill: var(--white); }
</style>
</head>
<body>

<svg width="0" height="0" style="position:absolute">
  <defs>
    <linearGradient id="silver-band" x1="0" y1="0" x2="0" y2="1">
      <stop offset="0" stop-color="var(--silver-light)"/>
      <stop offset="0.5" stop-color="var(--silver-mid)"/>
      <stop offset="1" stop-color="var(--silver-dark)"/>
    </linearGradient>
    <linearGradient id="red-swoosh" x1="0" y1="0" x2="1" y2="1">
      <stop offset="0" stop-color="var(--red)"/>
      <stop offset="1" stop-color="var(--red-dark)"/>
    </linearGradient>
    <linearGradient id="blister-fill" x1="0" y1="0" x2="1" y2="1">
      <stop offset="0" stop-color="#cfd6dc"/>
      <stop offset="1" stop-color="#9aa6b0"/>
    </linearGradient>
    <symbol id="label-base" viewBox="0 0 300 460">
      <rect width="300" height="460" fill="var(--white)"/>
      <path d="M0,345 C130,345 215,310 262,235 L238,242 L300,165 L300,385 L0,385 Z" fill="url(#red-swoosh)"/>
      <path d="M0,358 C140,358 230,330 300,290 L300,300 C230,342 140,370 0,370 Z" fill="var(--red-dark)" opacity="0.6"/>
      <rect x="0" y="385" width="300" height="60" fill="url(#silver-band)"/>
      <rect x="0" y="445" width="300" height="15" fill="var(--red-dark)"/>
    </symbol>
  </defs>
</svg>

<!-- 10-pill standard box -->
<div class="panel box-front">
  <svg viewBox="0 0 300 460">
    <use href="#label-base"/>
    <circle cx="150" cy="115" r="38" fill="var(--red)"/>
    <text class="brand-name" x="150" y="215" text-anchor="middle" font-size="62">KRILO</text>
    <text class="big-num" x="282" y="318" text-anchor="end" font-size="52">8</text>
    <text class="minute" x="284" y="342" text-anchor="end" font-size="19">minute</text>
    <rect x="10" y="397" width="84" height="36" rx="6" fill="var(--red)"/>
    <text class="count" x="52" y="422" text-anchor="middle" font-size="20">10 pill</text>
    <text class="claim" x="288" y="410" text-anchor="end" font-size="17">fast-acting</text>
    <text class="claim" x="288" y="431" text-anchor="end" font-size="17">chewable form</text>
  </svg>
</div>

<!-- 50-pill bottle label -->
<div class="panel bottle-large">
  <svg viewBox="0 0 300 460">
    <use href="#label-base"/>
    <circle cx="150" cy="115" r="38" fill="var(--red)"/>
    <text class="brand-name" x="150" y="215" text-anchor="middle" font-size="62">KRILO</text>
    <text class="big-num" x="282" y="318" text-anchor="end" font-size="52">8</text>
    <text class="minute" x="284" y="342" text-anchor="end" font-size="19">minute</text>
    <rect x="10" y="397" width="84" height="36" rx="6" fill="var(--red)"/>
    <text class="count" x="52" y="422" text-anchor="middle" font-size="20">50 pill</text>
    <text class="claim" x="288" y="410" text-anchor="end" font-size="17">fast-acting</text>
    <text class="claim" x="288" y="431" text-anchor="end" font-size="17">chewable form</text>
  </svg>
</div>

<!-- 20-pill bottle label -->
<div class="panel bottle-small">
  <svg viewBox="0 0 300 460">
    <use href="#label-base"/>
    <circle cx="150" cy="115" r="38" fill="var(--red)"/>
    <text class="brand-name" x="150" y="215" text-anchor="middle" font-size="62">KRILO</text>
    <text class="big-num" x="282" y="318" text-anchor="end" font-size="52">8</text>
    <text class="minute" x="284" y="342" text-anchor="end" font-size="19">minute</text>
    <rect x="10" y="397" width="84" height="36" rx="6" fill="var(--red)"/>
    <text class="count" x="52" y="422" text-anchor="middle" font-size="20">20 pill</text>
    <text class="claim" x="288" y="410" text-anchor="end" font-size="17">fast-acting</text>
    <text class="claim" x="288" y="431" text-anchor="end" font-size="17">chewable form</text>
  </svg>
</div>

<!-- Sample pack, inside with blister -->
<div class="panel sample-inside">
  <svg viewBox="0 0 170 280">
    <rect width="170" height="280" fill="var(--white)"/>
    <rect x="18" y="22" width="134" height="150" rx="10" fill="url(#blister-fill)" role="img" aria-label="Single-pill blister pocket"/>
    <path d="M0,215 C70,215 120,195 150,150 L138,154 L170,110 L170,235 L0,235 Z" fill="url(#red-swoosh)"/>
    <rect x="0" y="235" width="170" height="45" fill="url(#silver-band)"/>
  </svg>
</div>

<!-- Sample pack, front -->
<div class="panel sample-front">
  <svg viewBox="0 0 170 280">
    <rect width="170" height="280" fill="var(--white)"/>
    <circle cx="85" cy="55" r="22" fill="var(--red)"/>
    <text class="brand-name" x="85" y="118" text-anchor="middle" font-size="36">KRILO</text>
    <path d="M0,215 C70,215 120,195 150,150 L138,154 L170,110 L170,235 L0,235 Z" fill="url(#red-swoosh)"/>
    <text class="big-num" x="160" y="195" text-anchor="end" font-size="30">8</text>
    <text class="minute" x="161" y="210" text-anchor="end" font-size="11">minute</text>
    <rect x="0" y="235" width="170" height="45" fill="url(#silver-band)"/>
    <rect x="6" y="247" width="40" height="22" rx="4" fill="var(--red)"/>
    <text class="count" x="26" y="263" text-anchor="middle" font-size="11">1 pill</text>
    <text class="claim" x="164" y="253" text-anchor="end" font-size="10">fast-acting</text>
    <text class="claim" x="164" y="267" text-anchor="end" font-size="10">chewable form</text>
  </svg>
</div>

</body>
</html>
```